Design a building access mobile app for Tally by Halvorn Portal Systems

Hello, We're looking for an awesome designer to create an app design for our app Tally, by Halvorn Portal Systems. the mobile app allows employees open their office doors with their mobile phone. this means they don't have to use those plastic card badges or keys. We like clean modern design, dark and light themes. We don't have a logo yet.
Updates

Reason: Waiting on a couple designers to submit concepts

Target Market(s)

Commercial and employees

Industry/Entity Type

Building

Font styles to use
Sans Serif
Other font styles liked:
• Oswald extra light

Requirements
Must have
• nice clean design

```html
<!DOCTYPE html>
<html lang="en">
<head>
<meta charset="utf-8">
<title>Tally – Welcome</title>
<link rel="stylesheet" href="https://fonts.googleapis.com/css2?family=Oswald:wght@200;300;500&family=Roboto:wght@400;500&display=swap">
<style>
  :root {
    --brand-red: #b01d33;
    --brand-red-deep: #a8182d;
    --brand-red-light: #b9283e;
    --white: #ffffff;
    --muted: #d9c6ca;
    --rule: rgba(255,255,255,0.55);
  }
  * { box-sizing: border-box; margin: 0; padding: 0; }
  html, body { width: 675px; height: 1200px; overflow: hidden; }
  body { font-family: "Oswald", sans-serif; color: var(--white); background: var(--brand-red); }

  .screen { position: relative; width: 675px; height: 1200px; overflow: hidden; background: var(--brand-red); }

  .hallway-backdrop {
    position: absolute; inset: 0;
    background: linear-gradient(135deg, var(--brand-red-light) 0%, var(--brand-red) 45%, var(--brand-red-deep) 75%, var(--brand-red) 100%);
  }

  .status-bar {
    position: absolute; top: 0; left: 0; right: 0; height: 40px;
    display: flex; align-items: center; justify-content: space-between;
    padding: 0 8px 0 10px;
    font-family: "Roboto", sans-serif; font-weight: 500; font-size: 15px;
  }
  .status-bar .left, .status-bar .right { display: flex; align-items: center; gap: 6px; width: 130px; }
  .status-bar .right { justify-content: flex-end; gap: 4px; }
  .status-bar .time { position: absolute; left: 0; right: 0; text-align: center; pointer-events: none; }

  .brand { position: absolute; top: 150px; left: 0; right: 0; display: flex; flex-direction: column; align-items: center; }
  .brand-mark { width: 70px; height: 70px; background: var(--white); margin-top: 60px; }
  .brand-name { margin-top: 56px; font-weight: 500; font-size: 46px; line-height: 1; letter-spacing: 0.2px; }

  .welcome {
    position: absolute; top: 414px; left: 50px; right: 49px;
    display: flex; align-items: center; gap: 12px;
  }
  .welcome .rule { flex: 1; height: 1px; background: var(--rule); }
  .welcome h1 { font-weight: 200; font-size: 50px; line-height: 64px; color: var(--muted); white-space: nowrap; letter-spacing: -0.3px; }

  .actions { position: absolute; top: 1026px; left: 54px; right: 53px; display: flex; justify-content: space-between; }
  .btn {
    width: 257px; height: 84px;
    border: 2px solid var(--white); border-radius: 3px;
    display: flex; align-items: center; justify-content: center;
    font-family: "Oswald", sans-serif; font-weight: 300; font-size: 42px;
    color: var(--white); background: transparent; text-decoration: none;
  }
</style>
</head>
<body>
<main class="screen">
  <div class="hallway-backdrop" role="img" aria-label="Softly blurred photo of an office corridor with doors, tinted red"></div>

  <header class="status-bar">
    <div class="left">
      <svg width="48" height="10" viewBox="0 0 48 10" aria-hidden="true">
        <g fill="#fff"><circle cx="4" cy="5" r="4"/><circle cx="14" cy="5" r="4"/><circle cx="24" cy="5" r="4"/><circle cx="34" cy="5" r="4"/><circle cx="44" cy="5" r="4"/></g>
      </svg>
      <svg width="16" height="12" viewBox="0 0 16 12" aria-hidden="true">
        <path d="M8 11.5 L5.6 8.6 A3.6 3.6 0 0 1 10.4 8.6 Z" fill="#fff"/>
        <path d="M3.6 6.4 A6.4 6.4 0 0 1 12.4 6.4" stroke="#fff" stroke-width="1.8" fill="none"/>
        <path d="M1.2 3.9 A9.8 9.8 0 0 1 14.8 3.9" stroke="#fff" stroke-width="1.8" fill="none"/>
      </svg>
    </div>
    <span class="time">9:41 PM</span>
    <div class="right">
      <svg width="9" height="14" viewBox="0 0 9 14" aria-hidden="true">
        <path d="M1 4 L7 10 L4 13 V1 L7 4 L1 10" stroke="rgba(255,255,255,0.7)" stroke-width="1.3" fill="none"/>
      </svg>
      <span>100%</span>
      <svg width="32" height="14" viewBox="0 0 32 14" aria-hidden="true">
        <rect x="0.75" y="0.75" width="27.5" height="12.5" rx="2.5" stroke="#fff" stroke-width="1.5" fill="none"/>
        <rect x="2.5" y="2.5" width="24" height="9" rx="1" fill="#fff"/>
        <rect x="29.5" y="4.5" width="2" height="5" rx="1" fill="#fff"/>
      </svg>
    </div>
  </header>

  <section class="brand">
    <div class="brand-mark" aria-hidden="true"></div>
    <p class="brand-name">Halvorn security</p>
  </section>

  <section class="welcome">
    <span class="rule"></span>
    <h1>Welcome Halvorn security</h1>
    <span class="rule"></span>
  </section>

  <nav class="actions">
    <a class="btn btn-login" href="#">Log In</a>
    <a class="btn btn-signup" href="#">Sign Up</a>
  </nav>
</main>
</body>
</html>
```